Verdant Loop Advisors, LLC

I am looking for a simple, clear layout with my logo prominent and embossed, on the best quality card stock available. I would like the business name and phone number included on the card as well......I dont want my name anywhere on the card and I would like my logo embossed on the card......something simple with a white back......open to designs as long as they go along with recycling symbols and green type stuff.....The address, website, cell number, fax number, and email are listed below

5374 Tillbury Fenwood Road
Hyattsville, MD 20785

c. 240.555.0143 f. 240.555.0187
e. sales@verdantloopadvisors.example
w. www.verdantloopadvisors.example

Industry/Entity Type

Recycling

```html
<!DOCTYPE html>
<html lang="en">
<head>
<meta charset="utf-8">
<title>Verdant Loop Advisors, LLC — Business Card</title>
<link rel="stylesheet" href="https://fonts.googleapis.com/css2?family=Titillium+Web:wght@400;600&display=swap">
<style>
  :root {
    --page-bg: #d9d9d9;
    --card-top: #ffffff;
    --card-bottom: #e6e6e6;
    --green-dark: #245a36;
    --green-light: #4f7a5b;
    --ink: #333333;
    --label: #3f6b4b;
    --band-text: #e8efe9;
  }
  * { margin: 0; padding: 0; box-sizing: border-box; }
  html, body {
    width: 1200px;
    height: 1000px;
    overflow: hidden;
    background: var(--page-bg);
    font-family: "Titillium Web", sans-serif;
  }
  .card {
    position: absolute;
    left: 202px;
    top: 272px;
    width: 796px;
    height: 454px;
    background: linear-gradient(180deg, var(--card-top) 0%, var(--card-top) 30%, var(--card-bottom) 100%);
    overflow: hidden;
  }
  .brand {
    position: absolute;
    left: 60px;
    top: 84px;
    width: 300px;
    text-align: center;
  }
  .brand-mark {
    display: block;
    width: 196px;
    height: 196px;
    margin: 0 auto 38px;
    border-radius: 50%;
    background: var(--green-dark);
  }
  .brand-name {
    font-weight: 600;
    font-size: 22px;
    line-height: 1;
    color: var(--ink);
    white-space: nowrap;
  }
  .contact {
    position: absolute;
    right: 40px;
    top: 26px;
    text-align: right;
    color: var(--ink);
  }
  .contact-row {
    display: flex;
    justify-content: flex-end;
    align-items: baseline;
    gap: 9px;
    line-height: 28px;
  }
  .contact-label {
    font-size: 13px;
    letter-spacing: 0.5px;
    text-transform: uppercase;
    color: var(--label);
  }
  .contact-value { font-size: 22px; }
  .contact-value.email { font-size: 22px; margin-bottom: 3px; }
  .address {
    position: absolute;
    right: 40px;
    top: 196px;
    text-align: right;
    font-size: 22px;
    line-height: 28px;
    color: var(--ink);
    font-style: normal;
  }
  .footer-band {
    position: absolute;
    left: 0;
    bottom: 0;
    width: 796px;
    height: 62px;
  }
  .website {
    position: absolute;
    right: 40px;
    bottom: 14px;
    font-size: 18px;
    color: var(--band-text);
  }
</style>
</head>
<body>
  <div class="card">
    <div class="brand">
      <span class="brand-mark"></span>
      <div class="brand-name">Verdant Loop Advisors, LLC</div>
    </div>

    <div class="contact">
      <div class="contact-row"><span class="contact-label">Email</span><span class="contact-value email">sales@verdantloopadvisors.example</span></div>
      <div class="contact-row"><span class="contact-label">Phone</span><span class="contact-value">240 555 0143</span></div>
      <div class="contact-row"><span class="contact-label">Fax</span><span class="contact-value">240 555 0187</span></div>
    </div>

    <address class="address">
      5374 Tillbury Fenwood Road<br>
      Hyattsville, MD 20785
    </address>

    <svg class="footer-band" viewBox="0 0 796 62" aria-hidden="true">
      <defs>
        <radialGradient id="bandGlow" cx="0.58" cy="0.6" r="0.45">
          <stop offset="0" stop-color="#5b8466"/>
          <stop offset="1" stop-color="#245a36"/>
        </radialGradient>
      </defs>
      <rect x="0" y="40" width="420" height="22" fill="url(#bandGlow)"/>
      <polygon points="438,62 464,8 796,8 796,62" fill="url(#bandGlow)"/>
      <polygon points="414,4 466,0 456,26 446,16 426,56 412,56 434,12" fill="#2f6540"/>
    </svg>
    <div class="website">www.verdantloopadvisors.example</div>
  </div>
</body>
</html>
```